Redesign criminal justice consulting website

We run a small professional services firm that does research, evaluation, consulting, and training on criminal justice issues. We need to redesign our website (www.rvmetrics.com). The existing site is something we made ourselves. It is unprofessional and does not do a good job of communicating what we do or who we are.

We would like the new site to provide a basic overview of what we do. Moreover, we would like it to communicate several themes that represent who we are:

* global

* innovative

* analytical

* practical

We view the principal design challenge as figuring out a subtle, interesting, and graphically appealing way to communicate these themes.

Target Market(s)

Our primary customers are governments, research firms, criminal justice agencies, and schools. The people who we want to find our site are seeking research, evaluation, training, or consulting services related to crime, criminal justice, or policing.

Industry/Entity Type

Consulting

Number of Pages Required

2 pages

Requirements
Must have
• 1. We would like the site to use our logo. It is attached (please use the maroon 4-color version with the company name but without the slogan). The site should also use the colors present in our logo. It may use other colors as well, as long as these colors coordinate with the logo colors.

• 2. For main pages or buttons, we need the following:
• *Home
• *About RVM
• *Services
• *E-Training
• *Resources
• *Contact RVM

• 3. We like simple, crisp, subtle designs over "busier," cluttered, or very complex designs.

• 4. We'd like to receive, at a minimum, the home page and a sample inner page.
Nice to have
• We need some help in thinking through what regions or sections should exist on the home page. We are thinking about having a window on there where we can make announcements about recent developments like new reports, new e-training videos, new photographs, etc... We are open to suggestions here.
Should not have
• 1. Gimmicky or overused clipart.
• 2. Cliched images associated with criminal justice, including magnifying glasses, scales of justice, etc... Our logo makes a subtle nod to criminal justice through the use of a fingerprint as the dot on the "J" in the company initials. That''s sufficient for our purposes. Concentrate instead on the themes listed above.
• 3. Major use of colors that don't match our logo, like blue.

```html
<!DOCTYPE html>
<html lang="en">
<head>
<meta charset="utf-8">
<title>About RVM</title>
<link href="https://fonts.googleapis.com/css2?family=Source+Sans+3:wght@400;600&display=swap" rel="stylesheet">
<style>
  :root {
    --maroon: #b3173b;
    --banner: #bf7f43;
    --tab-active: #7a4a2a;
    --footer: #5a2d13;
    --ink: #1b1b1b;
    --line: #c8c8c8;
    --white: #ffffff;
    --footer-accent: #e0a060;
  }
  * { box-sizing: border-box; margin: 0; padding: 0; }
  html, body { width: 1200px; height: 1055px; overflow: hidden; background: var(--white); }
  body { position: relative; font-family: "Source Sans 3", sans-serif; color: var(--ink); }

  .brand { position: absolute; left: 38px; top: 22px; display: flex; align-items: center; gap: 10px; }
  .brand-mark { width: 14px; height: 14px; border-radius: 50%; background: var(--maroon); }
  .brand-name { font-size: 52px; font-weight: 600; color: var(--maroon); line-height: 1; letter-spacing: 1px; }
  .header-divider { position: absolute; left: 300px; top: 32px; width: 2px; height: 50px; background: #555; }
  .home-link { position: absolute; left: 336px; top: 46px; font-size: 18px; color: var(--ink); }
  .home-link .accent { color: var(--maroon); }
  .chev { margin-left: 8px; }

  .main-nav { position: absolute; left: 0; top: 97px; width: 1200px; height: 48px; border-top: 1px solid var(--line); }
  .nav-item { position: absolute; top: 0; height: 48px; display: flex; align-items: center; justify-content: center; font-size: 18px; font-weight: 600; color: var(--ink); border-right: 1px solid var(--line); }
  .nav-item .chev { color: #777; font-weight: 400; }
  .nav-item .accent { color: var(--maroon); margin-left: 5px; }
  .nav-item.is-active { top: -2px; height: 54px; background: var(--tab-active); color: var(--white); border-radius: 6px 6px 0 0; border: none; }
  .nav-item.is-active .accent { color: #1e0d04; }
  .nav-item.is-active .chev { color: var(--white); }
  .nav-item.contact { border-right: none; justify-content: flex-start; padding-left: 22px; }

  .hero { position: absolute; left: 0; top: 145px; width: 1200px; height: 332px; background: var(--banner); }
  .hero-title { position: absolute; left: 12px; top: 88px; width: 505px; font-size: 37px; font-weight: 400; line-height: 51px; color: #111; }
  .hero-title .lead { font-size: 49px; color: var(--white); }
  .hero-visual { position: absolute; top: 52px; height: 237px; }
  .hero-visual.flag { left: 521px; width: 306px; background: linear-gradient(135deg, #8e2a2a, #c9c4c0 45%, #6b4024); }
  .hero-visual.statue { left: 827px; width: 368px; background: linear-gradient(90deg, #7d8f88, #b9c1bc 55%, #f4f4f4); }

  .content { position: absolute; left: 74px; top: 528px; width: 1076px; }
  .page-heading { display: flex; align-items: baseline; gap: 8px; font-size: 21px; font-weight: 400; margin-left: 2px; margin-bottom: 38px; }
  .page-heading .accent { color: var(--maroon); font-size: 28px; font-weight: 600; }
  .content p { font-size: 13.2px; line-height: 17px; margin-bottom: 17px; }
  .content h2 { font-size: 13.2px; font-weight: 400; line-height: 17px; }

  .site-footer { position: absolute; left: 179px; top: 977px; width: 815px; height: 78px; background: var(--footer); color: var(--white); text-align: center; font-size: 13px; padding-top: 13px; line-height: 21px; }
  .site-footer .accent { color: var(--footer-accent); }
</style>
</head>
<body>
  <header>
    <div class="brand">
      <span class="brand-mark"></span>
      <span class="brand-name">RVM</span>
    </div>
    <div class="header-divider"></div>
    <a class="home-link"><span class="accent">RVM</span> Home<span class="chev">&gt;</span></a>
  </header>

  <nav class="main-nav">
    <a class="nav-item is-active" style="left:0;width:142px;">About<span class="accent">RVM</span><span class="chev">&gt;</span></a>
    <a class="nav-item" style="left:143px;width:180px;">Services<span class="chev">&nbsp;&nbsp;&gt;</span></a>
    <a class="nav-item" style="left:323px;width:164px;">E-Training<span class="chev">&nbsp;&gt;</span></a>
    <a class="nav-item" style="left:487px;width:153px;">Resources<span class="chev">&nbsp;&gt;</span></a>
    <a class="nav-item contact" style="left:640px;width:560px;">Contact<span class="accent">RVM</span><span class="chev">&gt;</span></a>
  </nav>

  <section class="hero">
    <h1 class="hero-title"><span class="lead">RVM operates</span> on a set of core principles that influence everything we do</h1>
    <div class="hero-visual flag" role="img" aria-label="Photo of a wooden gavel resting on an American flag"></div>
    <div class="hero-visual statue" role="img" aria-label="Photo of a justice statue holding scales"></div>
  </section>

  <main class="content">
    <div class="page-heading">About <span class="accent">RVM</span></div>
    <p>RVM operates on a set of core principles that influence everything we do.</p>
    <h2>1. ANALYSIS</h2>
    <p>Meaningful analysis is what we believe in and what we do best. Analysis is vital for planning successful change efforts in organizations. Knee-jerk change efforts that result from faulty impressions or incorrect assumptions often fail. Questioning routine practices, while often controversial, is essential.</p>
    <h2>2. INCLUSIVENESS</h2>
    <p>History teaches us that change efforts that exclude internal and external stakeholders are unlikely to succeed.</p>
    <h2>3. TAILORING AND CUSTOMIZATION</h2>
    <p>The most effective innovations are those that are tailored or customized to the specific and unique characteristics of each problem. Copying innovations from other jurisdictions is often ineffective and sometimes even counterproductive.</p>
    <h2>4. EVALUATION AND ASSESSMENT</h2>
    <p>Implementing effective change means evaluating and assessing the change effort at every stage, generating feedback from employees, clients, and other stakeholders, and then adapting as necessary.</p>
    <p>As external consultants, we seek to learn about our clients: their worldview, their environment, their frustrations and accomplishments, their sources of embarrassment and their sources of pride. We work with them as partners at every step in the process. Avoid at all costs any consultant who makes recommendations about your organization without taking the time to learn</p>
  </main>

  <footer class="site-footer">
    <div>Home - About RVM - Services - Clients - Contact</div>
    <div>Copyright © 2010 <span class="accent">RVM</span> . All Rights Reserved. Site Terms | General Terms &amp; Conditions | Privacy | Legal Notice</div>
  </footer>
</body>
</html>
```